Bramwick Client Journey To Success

I need a one-page document that graphically shows the client's journey working with Bramwick from initial assessment to completed project. I want the journey to start at the "basecamp logo" and reach 4 summits (little mountain logos...) .

I'd like the imagery to convey the client starting at basecamp, and moving to each summit. Each summit, should list the subtext under each, as listed on the pdf doc i provided.

The description for the basecamp and 4 summits is attached.

I need the brochure to look like the other brochure that you did for me (attached) .

Target Market(s)

Restaurant Owners

Industry/Entity Type

Construction Management

Font styles to use
Sans Serif

Colors
EB3D1F
EC4F4E
F09395
F8D3D4
FCEDEE

Requirements
Must have
• My logo. Title: Client Journey To Success. Subtitle: The 4 Summits

```html
<!DOCTYPE html>
<html lang="en">
<head>
<meta charset="utf-8">
<title>Bramwick Development – Client Journey To Success</title>
<link rel="stylesheet" href="https://fonts.googleapis.com/css2?family=Open+Sans:wght@400;600;700;800&display=swap">
<style>
  :root {
    --red: #eb3d1f;
    --coral: #ec4f4e;
    --salmon: #f09395;
    --blush: #f8d3d4;
    --mist: #fcedee;
    --ink: #111111;
    --title-dark: #3a1a14;
  }
  * { margin: 0; padding: 0; box-sizing: border-box; }
  html, body { width: 848px; height: 1200px; overflow: hidden; background: #ffffff; }
  .brochure {
    position: relative;
    width: 848px;
    height: 1200px;
    overflow: hidden;
    font-family: "Open Sans", sans-serif;
    color: #ffffff;
    background: linear-gradient(180deg, #f07f6e 47%, #ef6a57 70%, var(--red) 100%);
  }
  .hero-art { position: absolute; inset: 0; width: 848px; height: 1200px; }
  .brand {
    position: absolute; top: 40px; left: 0; width: 848px;
    text-align: center; color: var(--ink);
  }
  .brand-mark {
    display: inline-flex; align-items: center; gap: 10px;
    font-weight: 800; font-size: 34px; color: var(--coral);
  }
  .brand-mark .square { width: 26px; height: 26px; background: var(--red); }
  .brand-line { margin-top: 46px; font-weight: 700; font-size: 20px; letter-spacing: 0.5px; }
  .title {
    position: absolute; top: 188px; left: 0; width: 848px;
    text-align: center; font-weight: 700; line-height: 1;
  }
  .title-main, .title-sub {
    display: block;
    background: linear-gradient(180deg, #2a120e 20%, #8a2a1e 65%, var(--coral) 100%);
    -webkit-background-clip: text; background-clip: text;
    -webkit-text-fill-color: transparent;
    filter: drop-shadow(4px 4px 0 rgba(60,20,10,0.55));
  }
  .title-main { font-size: 92px; }
  .title-sub { font-size: 44px; margin-top: 10px; }
  .col { position: absolute; }
  .col-left { left: 18px; top: 0; }
  .col-right { left: 497px; top: 0; }
  .summits-heading {
    position: absolute; left: 18px; top: 628px;
    font-weight: 700; font-size: 48px; line-height: 1;
    text-shadow: 3px 3px 0 rgba(60,20,10,0.6);
  }
  .stage {
    position: absolute; white-space: nowrap;
    font-weight: 700; line-height: 1.2;
    text-decoration: underline; text-underline-offset: 4px; text-decoration-thickness: 2px;
  }
  .step { position: absolute; white-space: nowrap; font-weight: 600; line-height: 1.2; }
  .lg { font-size: 31.5px; }
  .md-left { font-size: 25px; }
  .md-right { font-size: 23px; }
  .stage-lg { font-size: 29px; }
  .stage-md { font-size: 27px; }
  .site {
    position: absolute; left: 535px; top: 1152px;
    font-weight: 800; font-size: 23px; color: var(--ink);
  }
</style>
</head>
<body>
<main class="brochure">
  <svg class="hero-art" viewBox="0 0 848 1200">
    <defs>
      <linearGradient id="sunset" x1="0" y1="0" x2="0" y2="1">
        <stop offset="0" stop-color="#6a4a1e"/>
        <stop offset="0.25" stop-color="#d89a32"/>
        <stop offset="0.4" stop-color="#f2c458"/>
        <stop offset="0.6" stop-color="#c99a50"/>
        <stop offset="0.8" stop-color="#7a5634"/>
        <stop offset="1" stop-color="#3e2618"/>
      </linearGradient>
      <linearGradient id="stripe" x1="0" y1="0" x2="0" y2="1">
        <stop offset="0" stop-color="#fcedee"/>
        <stop offset="1" stop-color="#f09395"/>
      </linearGradient>
    </defs>
    <polygon role="img" aria-label="Sunset photograph of a hiker at basecamp looking up a mountain ridge toward distant summits above misty valleys"
      points="0,0 848,0 848,567 511,567 431,673 352,567 0,567" fill="url(#sunset)"/>
    <line x1="8" y1="-6" x2="431" y2="673" stroke="url(#stripe)" stroke-width="14"/>
    <line x1="842" y1="-6" x2="431" y2="673" stroke="url(#stripe)" stroke-width="14"/>
  </svg>

  <header class="brand">
    <div class="brand-mark"><span class="square"></span>Bramwick</div>
    <div class="brand-line">BRAMWICK DEVELOPMENT</div>
  </header>

  <h1 class="title">
    <span class="title-main">Client Journey</span>
    <span class="title-sub">To Success</span>
  </h1>

  <h2 class="summits-heading">The 4 Summits</h2>

  <section class="col col-left">
    <h3 class="stage stage-lg" style="top:716px">1. Basecamp</h3>
    <p class="step lg" style="top:759px">a. Client Assessment</p>
    <p class="step lg" style="top:804px">b. Determine Project Goals</p>
    <p class="step lg" style="top:849px">c. Proposal &amp; Fees</p>

    <h3 class="stage stage-lg" style="top:915px">2. Summit 1 - PreConstruction</h3>
    <p class="step md-left" style="top:957px">a. Develop Project Plan</p>
    <p class="step md-left" style="top:994px">b. Develop Risk Assessment &amp; Plan</p>
    <p class="step md-left" style="top:1030px">c. Devlelop Schedule</p>
    <p class="step md-left" style="top:1068px">d. Develop Budget</p>
    <p class="step md-left" style="top:1105px">e. Develop Team</p>
    <p class="step md-left" style="top:1141px">f. GC, Sub, Consultants Contracts</p>
  </section>

  <section class="col col-right">
    <h3 class="stage stage-md" style="top:592px">3. Summit 2 - Execution</h3>
    <p class="step md-right" style="top:631px">a. Acquire Permits</p>
    <p class="step md-right" style="top:666px">b. PreConstruction Meeting</p>
    <p class="step md-right" style="top:701px">c. Project Start</p>

    <h3 class="stage stage-md" style="top:765px">4. Summit 3 -</h3>
    <h3 class="stage stage-md" style="top:805px">Project Management</h3>
    <p class="step md-right" style="top:846px">a. Shared Consciousness</p>
    <p class="step md-right" style="top:886px">&nbsp;Meetings.</p>
    <p class="step md-right" style="top:925px">b. Pressurized Collaboration</p>
    <p class="step md-right" style="top:964px">c. Schedule Management</p>
    <p class="step md-right" style="top:1003px">d. Run O.O.D.A. Loop</p>
    <h3 class="stage stage-md" style="top:1037px">5. Summit 4 - Completion</h3>
    <p class="step md-right" style="top:1080px">a. Closeout</p>
  </section>

  <p class="site">WWW.yourwebsite.com</p>
</main>
</body>
</html>
```